Ridgewell Stonecraft Construction Needs business card

Hey we are in need of business card designs. I have upload our logo as a guideline, but free feel to run with it or come up with something unique.
Pls have fun with it and be creative. the name says it all!
i will give some directions after i see a few entries..
Logo source file has been uploaded..
Hey because of the logo is so colourful already.
Can we have a few submissions with less colour.
Also we are looking for clever/hidden/descriptive business card.

```html
<!DOCTYPE html>
<html lang="en">
<head>
<meta charset="utf-8">
<title>Ridgewell Stonecraft Construction – Business Card</title>
<link href="https://fonts.googleapis.com/css2?family=Arimo:wght@400;700&display=swap" rel="stylesheet">
<style>
  :root {
    --backdrop: #e7e4df;
    --card: #ffffff;
    --ink: #111111;
    --ink-soft: #3a3a3a;
    --brand-grey: #6b6b6b;
    --accent-blue: #1c73c4;
    --accent-red: #d8141f;
    --accent-yellow: #f1c40f;
    --accent-green: #1d9a3a;
  }
  * { box-sizing: border-box; margin: 0; padding: 0; }
  html, body { width: 1200px; height: 800px; overflow: hidden; }
  body {
    background: var(--backdrop);
    font-family: "Arimo", Arial, sans-serif;
    display: flex;
    align-items: center;
    justify-content: center;
    gap: 60px;
  }
  .card {
    width: 525px;
    height: 300px;
    background: var(--card);
    box-shadow: 0 6px 18px rgba(0,0,0,0.12);
    position: relative;
    overflow: hidden;
  }

  /* Front side */
  .card-front {
    display: flex;
    flex-direction: column;
    align-items: center;
    justify-content: center;
  }
  .brand {
    display: flex;
    align-items: center;
    gap: 12px;
  }
  .brand-square {
    width: 22px;
    height: 22px;
    background: var(--accent-blue);
  }
  .brand-name {
    color: var(--brand-grey);
    font-weight: 700;
    font-size: 30px;
    letter-spacing: 0.5px;
    text-transform: uppercase;
    line-height: 1.1;
  }
  .brand-front .brand-name { text-align: left; }
  .web-address {
    position: absolute;
    bottom: 34px;
    left: 0;
    right: 0;
    text-align: center;
    color: var(--brand-grey);
    font-size: 13px;
  }

  /* Back / contact side */
  .card-contact { padding: 34px 0 0 34px; }
  .card-contact .brand-name { font-size: 19px; }
  .card-contact .brand-square { width: 16px; height: 16px; }
  .person { margin-top: 30px; }
  .person-name { font-size: 16px; font-weight: 700; color: var(--ink); }
  .person-role { font-size: 11px; color: var(--ink-soft); margin-top: 3px; }
  .address { margin-top: 16px; font-size: 11.5px; color: var(--ink-soft); line-height: 1.45; }
  .contact-list { list-style: none; margin-top: 14px; font-size: 11.5px; color: var(--ink); }
  .contact-list li { display: flex; align-items: center; gap: 10px; line-height: 1.55; }
  .contact-list svg { width: 11px; height: 11px; fill: var(--ink); flex: none; }
  .mark-decoration {
    position: absolute;
    top: 0;
    right: 0;
    width: 175px;
    height: 190px;
    background: linear-gradient(135deg, #f4d35e 0%, #e4525a 35%, #4b8fd6 70%, #3ca75a 100%);
    opacity: 0.85;
  }
</style>
</head>
<body>
  <section class="card card-front" aria-label="Card front">
    <div class="brand brand-front">
      <span class="brand-square"></span>
      <span class="brand-name">Ridgewell Stonecraft<br>Construction</span>
    </div>
    <p class="web-address">www.ridgewellstonecraft.com</p>
  </section>

  <section class="card card-contact" aria-label="Card back">
    <div class="brand">
      <span class="brand-square"></span>
      <span class="brand-name">Ridgewell Stonecraft<br>Construction</span>
    </div>
    <div class="person">
      <p class="person-name">Marco Delaney</p>
      <p class="person-role">Director</p>
    </div>
    <p class="address">Jalan Cemara 42B, Taman Sari<br>Kota Hilir - Indonesia 54321</p>
    <ul class="contact-list">
      <li>
        <svg viewBox="0 0 24 24" aria-hidden="true"><path d="M6.6 10.8a15.1 15.1 0 0 0 6.6 6.6l2.2-2.2a1 1 0 0 1 1-.25 11.4 11.4 0 0 0 3.6.57 1 1 0 0 1 1 1V20a1 1 0 0 1-1 1A17 17 0 0 1 3 4a1 1 0 0 1 1-1h3.5a1 1 0 0 1 1 1c0 1.25.2 2.45.57 3.6a1 1 0 0 1-.25 1z"/></svg>
        +62 (21) 555.010.2040
      </li>
      <li>
        <svg viewBox="0 0 24 24" aria-hidden="true"><path d="M7 1h10a2 2 0 0 1 2 2v18a2 2 0 0 1-2 2H7a2 2 0 0 1-2-2V3a2 2 0 0 1 2-2zm0 3v14h10V4zm5 15.5a1 1 0 1 0 0 2 1 1 0 0 0 0-2z"/></svg>
        +62 (08) 8100.432.7788
      </li>
      <li>
        <svg viewBox="0 0 24 24" aria-hidden="true"><path d="M2 5h20v14H2zm2 2v.5l8 5 8-5V7zm0 2.9V17h16V9.9l-8 5z"/></svg>
        marco@ridgewellstonecraft.com
      </li>
    </ul>
    <div class="mark-decoration" role="img" aria-label="Large colourful brand mark decoration in the top right corner"></div>
  </section>
</body>
</html>
```